Stationary design for construction company

Want professional stationary and in the future brochures to use for contacting potential customers and existing customers. We are open to suggestions with existing logo. We are a contractor in the construction field that specializes in foundation plastering. We currently do other work but are looking to market and become the only go-to subcontractor for this specialty. I like the red and black contrast and the font which is "biner d". We want to present ourselves as a professional company so potential customers take us seriously.
Brookvane Plaster
74 N. Maple #318
Orem, Utah 84092
801.555.0147 Office
801.555.0183 Mobile
maribel@brookvaneplaster.example
nolan@brookvaneplaster.example
We will need to be able to edit the finished work incase future numbers, addresses and such change.
Thx
Maribel
Target Market(s)
New and exiting customers in the building industry
Industry/Entity Type
Construction Company
Font styles to use
Other font styles liked:
- Biner D
Look and feel

```html
<!DOCTYPE html>
<html lang="en">
<head>
<meta charset="utf-8">
<title>Brookvane Plaster Stationery</title>
<link rel="stylesheet" href="https://fonts.googleapis.com/css2?family=Source+Sans+3:ital,wght@0,400;0,700;1,400&display=swap">
<style>
  :root {
    --backdrop: #a89474;
    --paper: #ffffff;
    --paper-shade: #f5f5f5;
    --brand-red: #cc0000;
    --ink: #1a1a1a;
    --text: #444444;
    --rule: #c8c8c8;
  }
  * { box-sizing: border-box; margin: 0; padding: 0; }
  html, body { width: 1200px; height: 770px; overflow: hidden; }
  body {
    background: var(--backdrop);
    font-family: "Source Sans 3", sans-serif;
    color: var(--text);
    position: relative;
    -webkit-font-smoothing: antialiased;
    -moz-osx-font-smoothing: grayscale;
  }
  .sheet { position: absolute; background: var(--paper); box-shadow: 0 2px 6px rgba(0,0,0,.25); }

  .brand { display: flex; align-items: center; gap: 6px; }
  .brand-square { background: var(--brand-red); flex: none; }
  .brand-name {
    font-family: "Source Sans 3", sans-serif; font-weight: 700; color: var(--ink);
    text-transform: uppercase; line-height: 1.05; letter-spacing: .5px;
  }

  /* Letterhead */
  .letterhead { left: 60px; top: 33px; width: 496px; height: 701px; }
  .letterhead .brand { position: absolute; left: 36px; top: 40px; }
  .letterhead .brand-square { width: 26px; height: 40px; }
  .letterhead .brand-name { font-size: 18px; }
  .letterhead .contact {
    position: absolute; left: 318px; top: 24px; padding-left: 12px;
    border-left: 1px solid var(--rule); font-size: 8.5px; line-height: 12px; color: var(--text);
    white-space: nowrap;
  }
  .contact-row { display: flex; align-items: center; gap: 5px; }
  .icon { width: 8px; height: 8px; flex: none; fill: var(--brand-red); }
  .salutation { position: absolute; left: 45px; top: 196px; font-size: 13px; color: var(--text); }
  .body-copy {
    position: absolute; left: 45px; top: 236px; width: 402px;
    font-size: 7.5px; line-height: 12px; color: var(--text); text-align: justify;
  }
  .body-copy p { margin-bottom: 12px; }
  .signoff { position: absolute; left: 45px; top: 489px; font-size: 7.5px; color: var(--text); }
  .signature { position: absolute; left: 42px; top: 507px; width: 66px; height: 26px; }
  .signer { position: absolute; left: 48px; top: 542px; font-size: 8.5px; line-height: 13px; color: var(--text); }
  .letter-url { position: absolute; left: 0; right: 0; top: 678px; text-align: center; font-size: 9px; font-style: italic; letter-spacing: 1px; color: var(--text); }

  /* Business card */
  .card { left: 720px; top: 30px; width: 246px; height: 140px; border: 1px solid #ddd; }
  .card-square { position: absolute; left: 12px; top: 4px; width: 90px; height: 132px; background: var(--brand-red); }
  .card-info { position: absolute; left: 126px; top: 10px; width: 112px; white-space: nowrap; }
  .card .brand-name { font-size: 16px; padding-bottom: 6px; border-bottom: 1px dotted #999; }
  .card-address { font-size: 6.5px; line-height: 9px; color: #333; padding: 5px 0 6px; border-bottom: 1px dotted #999; }
  .card-contacts { padding-top: 6px; font-size: 6.5px; line-height: 9.4px; color: #333; }
  .card .icon { width: 6px; height: 6px; }
  .card .contact-row { gap: 4px; }

  /* Envelope back */
  .envelope-back { left: 581px; top: 202px; width: 559px; height: 256px; background: var(--paper-shade); }
  .flap { position: absolute; left: 0; top: 0; width: 559px; height: 96px; }
  .flap-mark { position: absolute; left: 0; right: 0; top: 22px; display: flex; flex-direction: column; align-items: center; gap: 6px; }
  .flap-square { width: 29px; height: 44px; background: var(--paper); }
  .flap-url { font-size: 8px; font-style: italic; color: var(--paper); }

  /* Envelope front */
  .envelope-front { left: 579px; top: 480px; width: 560px; height: 253px; }
  .envelope-front .brand { position: absolute; left: 24px; top: 18px; }
  .envelope-front .brand-square { width: 26px; height: 40px; }
  .envelope-front .brand-name { font-size: 18px; }
  .return-address { position: absolute; left: 24px; top: 63px; font-size: 8.5px; color: var(--text); }
</style>
</head>
<body>

<svg width="0" height="0" style="position:absolute">
  <defs>
    <symbol id="icon-phone" viewBox="0 0 10 10"><path d="M2 0.5 L3.8 2.6 L2.9 3.7 Q4 6 6.3 7.1 L7.4 6.2 L9.5 8 L8.2 9.5 Q3 9 0.5 1.8 Z"/></symbol>
    <symbol id="icon-mobile" viewBox="0 0 10 10"><path d="M2.5 0 H7.5 V10 H2.5 Z M3.5 1 V8 H6.5 V1 Z" fill-rule="evenodd"/></symbol>
    <symbol id="icon-mail" viewBox="0 0 10 10"><path d="M0 2 H10 V8.5 H0 Z M0.8 2.6 L5 5.6 L9.2 2.6 Z" fill-rule="evenodd"/></symbol>
    <symbol id="icon-web" viewBox="0 0 10 10"><circle cx="5" cy="5" r="4.5"/></symbol>
  </defs>
</svg>

<section class="sheet letterhead">
  <div class="brand">
    <span class="brand-square"></span>
    <span class="brand-name">Brookvane<br>Plaster</span>
  </div>
  <div class="contact">
    <div>74 N. Maple #318</div>
    <div>Orem, Utah 84092</div>
    <div class="contact-row"><svg class="icon"><use href="#icon-phone"/></svg>801.555.0147</div>
    <div class="contact-row"><svg class="icon"><use href="#icon-mobile"/></svg>801.555.0183</div>
    <div class="contact-row"><svg class="icon"><use href="#icon-mail"/></svg>maribel@brookvaneplaster.example</div>
    <div class="contact-row"><svg class="icon"><use href="#icon-mail"/></svg>nolan@brookvaneplaster.example</div>
  </div>

  <p class="salutation">Dear Mr. Hollis,</p>
  <div class="body-copy">
    <p>Lorem ipsum dolor sit amet, consectetur adipiscing elit. Donec orci purus, luctus vitae dignissim eu, iaculis sed purus. Vivamus faucibus, ipsum nec aliquet viverra, leo mauris condimentum ligula, sit amet sagittis enim ligula quis arcu. Nam egestas tortor id nisi porttitor mattis. In tortor ante, ultricies in suscipit a, tempus non massa. Vivamus et auctor mi. Fusce vel massa nulla. Phasellus nec eros mauris, et scelerisque orci.</p>
    <p>Donec malesuada orci vitae nulla accumsan porta a id massa. Quisque accumsan iaculis magna sit amet fringilla. Maecenas consequat, magna eget tincidunt semper, odio nibh rutrum mi, id feugiat ante nisi eu risus. Vestibulum nunc orci, rhoncus a placerat in, ultricies in mi. Cras mattis varius eros, vel fringilla nisi suscipit eget. Quisque scelerisque sagittis nulla at porttitor.</p>
    <p>Sed id augue vitae urna euismod commodo aliquet a quam. Pellentesque arcu velit, cursus et malesuada ut, consequat et diam. Nullam erat sem, rhoncus id ullamcorper vitae, rhoncus et arcu. In ultricies ultricies nulla, ut rutrum nisi iaculis at. Donec eu magna a metus ornare faucibus. Fusce aliquet faucibus ultricies. Morbi semper, est id tincidunt gravida, sem arcu adipiscing lacus, ac bibendum nulla leo eu purus. Quisque nec diam sed risus consectetur a accumsan quis quis nibh. Vestibulum id purus lorem.</p>
    <p>It is a long established fact that a reader will be distracted by the readable content of a page when looking at its layout. The point of using Lorem Ipsum is that it has a more-or-less normal distribution of letters, as opposed to using ‘Content here, content here’, making it look like readable English. Many desktop publishing packages</p>
  </div>
  <p class="signoff">Sincerely,</p>
  <svg class="signature" role="img" aria-label="Handwritten signature"><rect width="66" height="26" fill="#e6e6e6"/></svg>
  <div class="signer">Dana Hollis<br>CEO/ Founder</div>
  <p class="letter-url">www.brookvaneplaster.example</p>
</section>

<section class="sheet card">
  <span class="card-square"></span>
  <div class="card-info">
    <div class="brand-name">Brookvane<br>Plaster</div>
    <div class="card-address">74 N. Maple #318<br>Orem, Utah 84092</div>
    <div class="card-contacts">
      <div class="contact-row"><svg class="icon"><use href="#icon-phone"/></svg>801.555.0147</div>
      <div class="contact-row"><svg class="icon"><use href="#icon-mobile"/></svg>801.555.0183</div>
      <div class="contact-row"><svg class="icon"><use href="#icon-mail"/></svg>maribel@brookvaneplaster.example</div>
      <div class="contact-row"><svg class="icon"><use href="#icon-mail"/></svg>nolan@brookvaneplaster.example</div>
      <div class="contact-row"><svg class="icon"><use href="#icon-web"/></svg>www.brookvaneplaster.example</div>
    </div>
  </div>
</section>

<section class="sheet envelope-back">
  <svg class="flap" viewBox="0 0 559 96" preserveAspectRatio="none">
    <path d="M0 0 H559 L548 62 Q543 94 515 94 H44 Q16 94 11 62 Z" fill="var(--brand-red)"/>
  </svg>
  <div class="flap-mark">
    <span class="flap-square"></span>
    <span class="flap-url">brookvaneplaster.example</span>
  </div>
</section>

<section class="sheet envelope-front">
  <div class="brand">
    <span class="brand-square"></span>
    <span class="brand-name">Brookvane<br>Plaster</span>
  </div>
  <p class="return-address">74 N. Maple #318. Orem, Utah 84092</p>
</section>

</body>
</html>
```